Democracy in crisis book

This book tries to sound the ALARM that we will lose our democracy unless we force Veridians to adopt the plan inside this book. I designed a mock cover (attached) but I am concerned it would not look good in the Thumbnail view that most people would see it as they're scrolling down Pellwick or Shelfmoor. The final title for the book is: Final Hour to Rescue the Shared Republic. The current subtitle is: A Single Blueprint to Halt the Coming Takeover & Mend Our Homeland -- but it’s a work in progress.The subtitle is still working progress but it's really not that important and can be small.
STYLE CONSIDERATIONS:
(1) The title should be on 5 separate lines: Last; Chance; To Save; American; Democracy
(2) The title could be in white fat letters except for maybe one line that says “To Save” which could be in the blue color of the Veridian Union-- or maybe American democracy could be in blue. We may have to try a few variations of that.
(3) I picked the red in the mock cover to connotate an emergency,
(4) I liked big bold fat font going across the full page so that it looks like a major warning sign, though note I was unable to extend each line flush all the way to the right which I think would have been better.
(5) I liked it better flush to left instead of centered.
(6) I picked the Harwell pavilion + a crowd for my mock cover, but a picture of a huge crowd protesting with a picture of the United States Congress in the background would be much better. DO NOT USE HARWELL. Obviously I would need it to be an open license or something I can pay a small amount to get. If you can find that picture then the page should probably be colored in red with Congress in white.
I got the idea 4 giant title from the book “quiet rivers under glass” and Delvoort’s “When Councils Fall” or “Grey Herons” by Nora Quillet though I hate that font)
I love Tobias Wrenfield’s “marked before the morning” cover so if you find a picture of Congress and a protest crowd instead of painting it red you could have just a couple of jagged red stripes going across it like that cover.
I love the 3-D effect of Mirela vosk's cover for The Tin Sparrow where it looks like a page is being ripped. That effect could be done the words American democracy like it's being torn off the page UPDATE: MANY DESIGNERS TRIED THAT & IT DID NOT WORK AT ALL.
Note that this book will be submitted to many award competitions, so please give me an award-winning cover.
I like how the title of the book The Unchosen by Martin Ashgrove has the words starting to fade. I don't like the ladder on it, but maybe 'American democracy' could fade like that.
Veridians

```html
<!DOCTYPE html>
<html lang="en">
<head>
<meta charset="utf-8">
<title>Final Hour to Rescue the Shared Republic — Cover</title>
<link rel="stylesheet" href="https://fonts.googleapis.com/css2?family=Archivo:wdth,wght@100,700;125,900&family=Libre+Baskerville:wght@700&display=swap">
<style>
  :root {
    --page: #ffffff;
    --frame: #9a9a9a;
    --alarm-red: #c8202b;
    --alarm-red-deep: #9e1620;
    --union-blue: #1c2f7a;
    --title-white: #ffffff;
    --photo-light: #f4f2ee;
    --photo-mid: #c9c6c2;
    --photo-deep: #6e6b6e;
  }
  html, body {
    margin: 0;
    padding: 0;
    width: 888px;
    height: 1200px;
    overflow: hidden;
    background: var(--page);
  }
  .canvas {
    position: relative;
    width: 888px;
    height: 1200px;
    box-sizing: border-box;
    border: 1px solid var(--frame);
    background: var(--page);
  }
  .cover {
    position: absolute;
    left: 48px;
    top: 39px;
    width: 792px;
    height: 1121px;
    background: var(--alarm-red);
    overflow: hidden;
  }
  .title-block {
    position: absolute;
    left: 0;
    top: 0;
    width: 792px;
    height: 620px;
  }
  .title-line {
    font-family: "Archivo", "Arial Black", sans-serif;
    font-weight: 900;
    font-stretch: 125%;
    fill: var(--title-white);
  }
  .title-line--accent { fill: var(--union-blue); }
  .subtitle {
    position: absolute;
    left: 36px;
    top: 630px;
    margin: 0;
    font-family: "Archivo", Arial, sans-serif;
    font-weight: 700;
    font-size: 20px;
    line-height: 27px;
    color: var(--title-white);
  }
  .author {
    position: absolute;
    left: 36px;
    top: 700px;
    margin: 0;
    font-family: "Libre Baskerville", Georgia, serif;
    font-weight: 700;
    font-size: 24px;
    line-height: 30px;
    color: var(--title-white);
  }
  .capitol-crowd-photo {
    position: absolute;
    left: 0;
    top: 752px;
    width: 792px;
    height: 369px;
    background: linear-gradient(to bottom,
      var(--photo-light) 0%,
      var(--photo-mid) 55%,
      var(--photo-deep) 100%);
  }
  .photo-stripes {
    position: absolute;
    left: 0;
    top: 752px;
    width: 792px;
    height: 369px;
  }
</style>
</head>
<body>
<div class="canvas">
  <div class="cover">
    <svg class="title-block" viewBox="0 0 792 620">
      <title>Final Hour to Rescue the Shared Republic</title>
      <text class="title-line" x="36" y="170" font-size="140" textLength="720" lengthAdjust="spacingAndGlyphs">FINAL</text>
      <text class="title-line" x="36" y="290" font-size="140" textLength="720" lengthAdjust="spacingAndGlyphs">HOUR</text>
      <text class="title-line title-line--accent" x="36" y="390" font-size="110" textLength="720" lengthAdjust="spacingAndGlyphs">TO RESCUE</text>
      <text class="title-line" x="36" y="490" font-size="110" textLength="720" lengthAdjust="spacingAndGlyphs">THE SHARED</text>
      <text class="title-line" x="36" y="600" font-size="120" textLength="720" lengthAdjust="spacingAndGlyphs">REPUBLIC</text>
    </svg>

    <p class="subtitle">A Single Blueprint to Halt the Coming<br>Takeover &amp; Mend Our Homeland</p>

    <p class="author">Calder Scott Mc Brennan</p>

    <div class="capitol-crowd-photo" role="img" aria-label="Photograph of a huge protest crowd in front of the white domed Congress building"></div>

    <svg class="photo-stripes" viewBox="0 0 792 369" aria-hidden="true">
      <path fill="var(--alarm-red)" d="M0 150 L760 132 L775 140 L762 147 L792 152 L792 178 L770 176 L782 184 L0 200 Z"/>
      <path fill="var(--alarm-red-deep)" d="M0 268 L740 250 L756 259 L744 266 L792 270 L792 296 L760 295 L772 304 L0 318 Z"/>
    </svg>
  </div>
</div>
</body>
</html>
```